New Business Card Fairway Nine and MRCC

Create a business card for golf instructor

Target Market(s)

Golf

Contact Information for Business Card

I teach golf at my indoor facility (Fairway Nine Golf) and I teach at a nearby golf course (Maple Ridge Country Club) I am the Director of Instruction at both. I would like to see designs that include both my logo and the golf course logo.
Dennis Wrayburn, TSL
Director of Instruction
Fairway Nine Golf Inc.
4362 Orchard Vale Rd
Suite F
Cincinnati, OH 45871
My business slogan: Swing is Good. Fairway Nine is Better. Go Further
www.fairwaynine-example.com
e: info@fairwaynine-example.com
p: 513-555-0187

Font styles to use
Sans Serif

Requirements
Nice to have
• Red, White, Black, Grey Colors

```html
<!DOCTYPE html>
<html lang="en">
<head>
<meta charset="utf-8">
<title>Fairway Nine Golf and MRCC Business Card</title>
<link rel="stylesheet" href="https://fonts.googleapis.com/css2?family=Roboto:wght@400;500;700&display=swap">
<style>
  :root {
    --backdrop: #e9e9ea;
    --card: #2d2d2e;
    --red: #e8413c;
    --ring: #5a5a5c;
    --green: #2f6b34;
    --muted: #8a8a8a;
  }
  * { margin: 0; padding: 0; box-sizing: border-box; }
  html, body { width: 1200px; height: 801px; overflow: hidden; }
  body {
    background: var(--backdrop);
    font-family: "Roboto", Arial, sans-serif;
    position: relative;
  }
  .card {
    position: absolute;
    top: 252px;
    width: 520px;
    height: 297px;
    background: var(--card);
    border-bottom: 3px solid var(--red);
    border-left: 2px solid var(--red);
    box-shadow: 0 10px 24px rgba(0,0,0,.22);
    overflow: hidden;
    color: var(--red);
  }
  .card--front { left: 50px; }
  .card--back { left: 630px; }

  /* front */
  .brand {
    position: absolute;
    top: 38px;
    left: 0; right: 0;
    display: flex;
    justify-content: center;
    align-items: center;
    gap: 12px;
  }
  .brand__dot {
    width: 34px; height: 34px;
    border: 3px solid var(--red);
    border-radius: 50%;
  }
  .brand__name { font-size: 30px; font-weight: 700; letter-spacing: .2px; }
  .brand__tagline {
    position: absolute;
    top: 82px; left: 0; right: 0;
    text-align: center;
    font-size: 10px;
  }
  .rule-top {
    position: absolute;
    top: 112px; left: 220px; right: 24px;
    height: 1px; background: var(--red);
  }
  .address {
    position: absolute;
    top: 128px; right: 28px;
    font-size: 12.5px;
    line-height: 1.35;
    text-align: left;
  }
  .person {
    position: absolute;
    left: 28px; top: 178px;
  }
  .person__name { font-size: 19px; font-weight: 500; }
  .person__title { font-size: 13px; margin-top: 1px; }
  .person__rule { width: 170px; height: 1px; background: var(--red); margin: 8px 0 7px; }
  .contacts { list-style: none; font-size: 12.5px; line-height: 1.45; }
  .contacts li { display: flex; align-items: center; gap: 8px; }
  .contacts svg { width: 11px; height: 11px; flex: none; }

  /* back */
  .ring {
    position: absolute;
    left: -70px; top: 110px;
  }
  .club {
    position: absolute;
    top: 70px; right: 40px;
    width: 260px;
    display: flex; flex-direction: column; align-items: center; gap: 10px;
  }
  .club__mark { width: 56px; height: 56px; background: var(--green); }
  .club__name {
    font-size: 20px; font-weight: 500; color: var(--green);
    text-align: center; line-height: 1.2;
  }
  .slogan {
    position: absolute;
    right: 22px; bottom: 34px;
    font-size: 13.5px; font-weight: 500;
  }
</style>
</head>
<body>

  <section class="card card--front" aria-label="Business card front">
    <div class="brand">
      <span class="brand__dot"></span>
      <span class="brand__name">Fairway Nine Golf</span>
    </div>
    <p class="brand__tagline">Swing is Good. Fairway Nine is Better. Go Further</p>
    <div class="rule-top"></div>

    <address class="address" style="font-style:normal">
      4362 Orchard Vale Rd<br>
      Suite F<br>
      Cincinnati, OH 45871
    </address>

    <div class="person">
      <p class="person__name">Dennis Wrayburn</p>
      <p class="person__title">Manager</p>
      <div class="person__rule"></div>
      <ul class="contacts">
        <li>
          <svg viewBox="0 0 12 12" aria-hidden="true"><path d="M2.5 1h2l1 3-1.3 1a7 7 0 0 0 2.8 2.8l1-1.3 3 1v2a1 1 0 0 1-1 1A9 9 0 0 1 1.5 2a1 1 0 0 1 1-1z" fill="currentColor"/></svg>
          513-555-0187
        </li>
        <li>
          <svg viewBox="0 0 12 12" aria-hidden="true"><rect x="1" y="2.5" width="10" height="7" fill="none" stroke="currentColor" stroke-width="1.3"/><path d="M1 3l5 3.5L11 3" fill="none" stroke="currentColor" stroke-width="1.3"/></svg>
          info@fairwaynine-example.com
        </li>
        <li>
          <svg viewBox="0 0 12 12" aria-hidden="true"><circle cx="6" cy="6" r="5" fill="none" stroke="currentColor" stroke-width="1.3"/><path d="M1 6h10M6 1c-2.5 3-2.5 7 0 10M6 1c2.5 3 2.5 7 0 10" fill="none" stroke="currentColor" stroke-width="1"/></svg>
          www.fairwaynine-example.com
        </li>
      </ul>
    </div>
  </section>

  <section class="card card--back" aria-label="Business card back">
    <svg class="ring" width="300" height="300" viewBox="0 0 300 300" aria-hidden="true">
      <circle cx="150" cy="150" r="130" fill="none" stroke="var(--ring)" stroke-width="18" opacity=".7"/>
    </svg>
    <div class="club">
      <span class="club__mark"></span>
      <p class="club__name">Maple Ridge Country Club</p>
    </div>
    <p class="slogan">Swing is Good. Fairway Nine is Better. Go Further</p>
  </section>

</body>
</html>
```